SALT PAN COMPUTERS AD DESIGN

This is to go into our local phone book as a full page (A4) advert.

NOTE THAT THE DEADLINE IS MIDNIGHT SUNDAY THE 29TH AUSSIE WA TIME NOT THE ADVERTISED DEADLINE AS FOR THE LIFE OF ME I CANT SEE WHERE TO CHANGE IT.

HAPPY TO PAY EXTRA FOR A "YES THATS IT" JOB.

Title - SALT PAN COMPUTERS

(THINGS TO HAVE)
24/7 FULL COMPUTER SERVICES
ALL COMPUTER PROBLEMS SOLVED
info@saltpancomputers.com.au
0400 13 8562
SALTPANCOMPUTERS.COM.AU
Virus's Removed
Data Recovery
Custom Computers and Programs built
Picked up & Dropped off
Private and Business Welcome

Maybe this photo - http://www.pixelvaultlib.com/stock-photo-22810457-attractive-receptionist.php?st=a3e91f2
with 24/7 service.

http://www.pixelvaultlib.com/stock-photo-22936104-hard-disk-drive-service.php?st=7d2f5e8 with Data Recovery

http://www.pixelvaultlib.com/stock-illustration-5318890-laptop.php?st=e14b7c9

I don't know but I have less than 40 hours to do this...

Been extented for another 50 hours cause they stuffed up also I have just opened a logo one as well.

Reason: As the publisher stuffed up with my account I now have an extra 50 hours !!

please note increased payment, this may increase again.

Reason: Not ment to finish for another 18 hours !!!!!!

Keep Going !!!!

only 5 hours left before it has to be at the printers !!!!

• only have 40 hours left from now. it must be in by 7am Monday 30th western aussie time. (not eastern aussie time)
• A 3D look
Colors like dark blue, bright yellow black and dark red.
modern look
modern font ie..HandelGothicBT etc

```html
<!DOCTYPE html>
<html lang="en">
<head>
<meta charset="utf-8">
<title>Salt Pan Computers – Phone Book Advert</title>
<link rel="stylesheet" href="https://fonts.googleapis.com/css2?family=Tinos:wght@700&display=swap">
<style>
  :root {
    --page-blue: #3a34f2;
    --plate-light: #8a8a8a;
    --plate-mid: #5e5e5e;
    --plate-dark: #2c2c2c;
    --letter-red: #ff2b2b;
    --letter-edge: #2a0000;
  }
  html, body {
    margin: 0;
    padding: 0;
    width: 900px;
    height: 1200px;
    overflow: hidden;
    background: var(--page-blue);
  }
  .advert {
    position: relative;
    width: 900px;
    height: 1200px;
    background: linear-gradient(160deg, #3d37f5 0%, var(--page-blue) 60%, #3530e6 100%);
    font-family: "Tinos", "Times New Roman", serif;
    font-weight: 700;
  }
  .plate {
    position: absolute;
    display: flex;
    align-items: center;
    justify-content: center;
    box-sizing: border-box;
    background: linear-gradient(180deg, var(--plate-light) 0%, var(--plate-mid) 45%, var(--plate-dark) 100%);
    border-top: 4px solid #b4b4b4;
    border-left: 4px solid #9a9a9a;
    border-bottom: 5px solid #161616;
    border-right: 5px solid #1e1e1e;
    box-shadow: 4px 5px 0 rgba(0,0,0,0.55);
    color: var(--letter-red);
    white-space: nowrap;
    letter-spacing: -1.5px;
    -webkit-text-stroke: 1.2px var(--letter-edge);
    text-shadow: 2px 2px 0 #111, -1px -1px 0 #d8d8d8;
  }
  .plate--title {
    left: 132px; top: 21px; width: 633px; height: 84px;
    font-size: 58px;
    letter-spacing: -1px;
  }
  .plate--line { font-size: 36px; height: 60px; }
  .plate--slim { font-size: 34px; height: 58px; }

  .line-service  { left: 183px; top: 300px; width: 537px; }
  .line-problems { left: 145px; top: 364px; width: 615px; }
  .line-email    { left: 213px; top: 430px; width: 477px; }
  .line-phone    { left: 348px; top: 495px; width: 210px; }
  .line-site     { left: 188px; top: 561px; width: 535px; }
  .line-virus    { left: 321px; top: 625px; width: 267px; }
  .line-recovery { left: 336px; top: 691px; width: 237px; }
  .line-custom   { left: 155px; top: 756px; width: 598px; }
  .line-pickup   { left: 263px; top: 820px; width: 382px; }
  .line-private  { left: 218px; top: 885px; width: 469px; }

  .photo {
    position: absolute;
  }
  .photo--receptionist {
    left: 75px; top: 140px; width: 175px; height: 135px;
    background: linear-gradient(135deg, #c9d9a0 0%, #f2e6b0 45%, #e8c890 100%);
  }
  .photo--hard-drive {
    left: 339px; top: 135px; width: 165px; height: 137px;
    background: radial-gradient(circle at 55% 45%, #d8dde2 0%, #8d959c 45%, #3d4247 100%);
  }
  .photo--laptop {
    left: 642px; top: 140px; width: 183px; height: 138px;
    background: linear-gradient(180deg, #2a2a2a 0%, #555 55%, #b8bcc0 80%, #8d9196 100%);
    border-radius: 4px 4px 8px 8px;
  }
</style>
</head>
<body>
<main class="advert">
  <h1 class="plate plate--title">SALT PAN COMPUTERS</h1>

  <div class="photo photo--receptionist" role="img" aria-label="Photo of a smiling receptionist wearing a headset"></div>
  <div class="photo photo--hard-drive" role="img" aria-label="Photo of an open hard disk drive"></div>
  <div class="photo photo--laptop" role="img" aria-label="Illustration of an open silver laptop"></div>

  <p class="plate plate--line line-service">24/7 FULL COMPUTER SERVICES</p>
  <p class="plate plate--line line-problems">ALL COMPUTER PROBLEMS SOLVED</p>
  <p class="plate plate--line line-email">info@saltpancomputers.com.au</p>
  <p class="plate plate--line line-phone">0400 13 8562</p>
  <p class="plate plate--line line-site">SALTPANCOMPUTERS.COM.AU</p>
  <p class="plate plate--slim line-virus">Virus's Removed</p>
  <p class="plate plate--slim line-recovery">Data Recovery</p>
  <p class="plate plate--line line-custom">Custom Computers and Programs built</p>
  <p class="plate plate--line line-pickup">Picked up &amp; Dropped off</p>
  <p class="plate plate--line line-private">Private and Business Welcome</p>
</main>
</body>
</html>
```